Small Graphic design business needs a marketing flyer

A small graphic design business called Marmot Studio needs an uplift with a trendy, catchy and creative A5 marketing flyer to promote their services. Their services include all aspects of graphic design from corporate branding to brochures, business cards and annual reports, and will take their clients right through to the final printed product.
Logo colours are shades of dark green to lime green, grey and black - see attached. We would like to see some of those colours carried through the design in some way, but not a necessity. The overall feel of the flyer to be eye-catching and enticing, clever, fun and bold to attract customers.

Target Market(s)

Anyone who wants to promote their business.

Industry/Entity Type

Graphic Design

Requirements
Must have
• • Must be A5 size
• Include this bit of text:
'Whether it’s a creative logo design, business stationery, ads, brochures, or even typesetting you're after, Marmot Studio can cater to all your design as well as printing needs. We will take you through from beginning to end, from creative design solutions, to the final printed product. We’re here to make things easy for you...to take your business to the next level.

• As far as other wording/heading goes to promote the business, I will leave it to your creativity but must include the promotion stating: 'Mention this flyer to receive 20% off all artwork and 10% off all printing.'

• Contact details to be included too:
Phone (08) 5137 4091
Email: marmot.studio@brelnet.example.au

• Please also include the logo and images (showing some samples of the companies work) attached.

Nice to have
• Would be nice to have some kind of promotion on the flyer e.g. 'if you mention this flyer you will receive 20% off....' or something to that effect.

```html
<!DOCTYPE html>
<html lang="en">
<head>
<meta charset="utf-8">
<title>Marmot Studio – Flyer</title>
<link href="https://fonts.googleapis.com/css2?family=Didact+Gothic&family=Arimo:wght@400;700&display=swap" rel="stylesheet">
<style>
  :root {
    --lime: #a6d176;
    --lime-soft: #d9ecc4;
    --leaf: #5a9a32;
    --ink: #231f20;
    --grey-band: #d9d9d9;
    --navy: #17264a;
    --orange: #f39a3c;
    --sky: #3aa8dc;
    --paper: #ffffff;
  }
  * { margin: 0; padding: 0; box-sizing: border-box; }
  html, body { width: 1200px; height: 900px; overflow: hidden; background: var(--paper); }
  .canvas { position: relative; width: 1200px; height: 900px; }

  .flyer {
    position: absolute; left: 306px; top: 42px; width: 562px; height: 796px;
    background: linear-gradient(180deg, var(--lime) 0%, var(--lime-soft) 55%, var(--paper) 80%);
    border: 1px solid #9a9a9a;
    box-shadow: 8px 10px 14px rgba(0,0,0,0.28);
    overflow: hidden;
  }

  .sample { position: absolute; left: 25px; width: 197px; border: 4px solid var(--leaf); background: var(--paper); overflow: hidden; }
  .sample--brochure { top: 28px; height: 275px; }
  .sample--cards { top: 311px; height: 150px; background: #fafafa; }
  .sample--engineer { top: 471px; height: 64px; }

  .brochure { position: absolute; left: 10px; top: 10px; width: 170px; height: 247px; border: 1px solid #ccc; }
  .brochure__head { height: 27px; background: var(--navy); color: #fff; font-family: "Arimo", sans-serif; font-weight: 700; font-size: 8.5px; line-height: 10px; padding: 3px 5px; position: relative; }
  .brochure__brand { position: absolute; right: 5px; top: 9px; font-size: 7px; font-weight: 400; }
  .brochure__photo { height: 93px; background: linear-gradient(160deg, #eef1f3 0%, #d8c6b2 60%, #b9a48d 100%); }
  .brochure__body { height: 113px; background: linear-gradient(180deg, var(--orange) 0%, #fbe2c6 18%, #fff 35%); padding: 3px 5px; font-family: "Arimo", sans-serif; font-size: 3.4px; line-height: 5px; color: #333; }
  .brochure__title { font-size: 6px; font-weight: 700; color: var(--navy); line-height: 9px; margin-bottom: 3px; }
  .brochure__cols { display: flex; gap: 5px; }
  .brochure__cols ul { list-style: none; flex: 1; }
  .brochure__foot { height: 14px; background: var(--navy); color: #fff; font-family: "Arimo", sans-serif; font-size: 3.4px; line-height: 14px; padding: 0 6px; display: flex; justify-content: space-between; }

  .card { position: absolute; top: 10px; width: 80px; height: 127px; background: #fff; font-family: "Arimo", sans-serif; color: #444; }
  .card--back { left: 12px; box-shadow: 2px 2px 3px rgba(0,0,0,0.3); padding: 8px 6px; font-size: 3.6px; line-height: 5px; }
  .card__name { font-weight: 700; color: var(--ink); }
  .card__mark { position: absolute; left: 8px; bottom: 12px; font-size: 8px; font-weight: 700; color: var(--leaf); }
  .card--front { left: 98px; border: 3px solid #111; box-shadow: 2px 2px 3px rgba(0,0,0,0.3); }
  .card__logo { height: 56px; display: flex; align-items: center; justify-content: center; font-size: 11px; font-weight: 700; color: var(--leaf); }
  .card__colour { height: 62px; background: var(--sky); border-top: 3px solid #111; }

  .engineer { height: 100%; display: flex; flex-direction: column; align-items: center; justify-content: center; font-family: "Arimo", sans-serif; color: #111; }
  .engineer__name { font-size: 28px; font-weight: 700; line-height: 30px; letter-spacing: -0.5px; }
  .engineer__tag { font-size: 6px; font-weight: 700; letter-spacing: 0.5px; align-self: flex-end; margin-right: 8px; }

  .headline { position: absolute; left: 238px; top: 24px; width: 284px; text-align: center; font-family: "Didact Gothic", sans-serif; font-size: 80px; line-height: 91px; color: var(--ink); font-weight: 400; }

  .services { position: absolute; left: 242px; top: 384px; width: 310px; font-family: "Arimo", sans-serif; font-size: 12.6px; line-height: 18.7px; color: var(--ink); }

  .brand { position: absolute; left: 150px; top: 578px; width: 270px; text-align: center; font-family: "Didact Gothic", sans-serif; color: #555; }
  .brand__name { font-size: 30px; line-height: 36px; display: inline-flex; align-items: center; gap: 8px; }
  .brand__dot { width: 12px; height: 12px; border-radius: 50%; background: var(--leaf); display: inline-block; }
  .brand__tag { font-size: 10px; line-height: 14px; margin-left: 60px; }

  .contact { position: absolute; left: 0; width: 100%; top: 640px; text-align: center; font-family: "Arimo", sans-serif; font-weight: 700; font-size: 13.5px; color: var(--ink); word-spacing: 1px; }
  .contact span + span { margin-left: 14px; }

  .promo { position: absolute; left: 0; top: 666px; width: 100%; height: 110px; border-top: 8px solid var(--leaf); border-bottom: 8px solid var(--leaf); background: var(--grey-band); text-align: center; font-family: "Didact Gothic", sans-serif; font-size: 30px; line-height: 37px; color: var(--ink); padding-top: 11px; }
</style>
</head>
<body>
<div class="canvas">
  <article class="flyer">

    <figure class="sample sample--brochure">
      <div class="brochure">
        <div class="brochure__head">GROWTH<br>PLANNER<span class="brochure__brand">Harbourline</span></div>
        <div class="brochure__photo" role="img" aria-label="Photo of a young family relaxing together on a beach"></div>
        <div class="brochure__body">
          <p class="brochure__title">Growth Planner Service Package</p>
          <div class="brochure__cols">
            <ul>
              <li>Review current goals and cash flow</li>
              <li>Plan savings and super strategy</li>
              <li>Review insurance and protection needs</li>
              <li>Tax planning and structure advice</li>
              <li>Estate planning and wills check</li>
              <li>Ongoing portfolio review each year</li>
            </ul>
            <ul>
              <li>Annual review meeting</li>
              <li>Strategy update and report</li>
              <li>Market news each quarter</li>
              <li>Access to your adviser</li>
            </ul>
          </div>
        </div>
        <div class="brochure__foot"><span>Growth Planner</span><span>Contact</span><span>Website</span></div>
      </div>
    </figure>

    <figure class="sample sample--cards">
      <div class="card card--back">
        <p class="card__name">Jamie Holt</p>
        <p>Managing Director</p>
        <p>&nbsp;</p>
        <p>Level 2, 14 Quay Street, Perth WA 6000</p>
        <p>P. 0400 000 000</p>
        <p>jamie@cartlane.example</p>
        <p class="card__mark">Cartlane</p>
      </div>
      <div class="card card--front">
        <div class="card__logo">Cartlane</div>
        <div class="card__colour"></div>
      </div>
    </figure>

    <figure class="sample sample--engineer">
      <div class="engineer">
        <span class="engineer__name">Voltbridge</span>
        <span class="engineer__tag">ELECTRONIC ENGINEERS</span>
      </div>
    </figure>

    <h1 class="headline">Let us design your next job!</h1>

    <p class="services">Our services include all aspects of graphic design<br>from logo design, business stationery, ads,<br>brochures, or even typesetting, Marmot Studio<br>can cater to all your design requirements as well<br>as printing needs. We will take you through from<br>beginning to end, from creative brief solutions, to the<br>final printed product. We're here to make things easy<br>for you and take your business to the next level.</p>

    <div class="brand">
      <p class="brand__name"><span class="brand__dot"></span>Marmot Studio</p>
      <p class="brand__tag">communication by design</p>
    </div>

    <p class="contact"><span>Phone (08) 5137 4091</span><span>Email: marmot.studio@brelnet.example.au</span></p>

    <p class="promo">Mention this flyer and receive 20%<br>off all artwork and 10% off all printing</p>
  </article>
</div>
</body>
</html>
```